Geschäftspapiere für gemeinnützige Organisation im weltweiten Bildungsbereich
Zielgruppe
Wir sind eine gemeinnützige Organisation mit Projekten im Bildungsbereich weltweit. Unsere Zielgruppe sind andere gemeinnützige Organisationen und Studenten.
Aufgabenstellung
Das Logo sollte aud das Geschäftspapier sowie änhnliche Farben bei den Informationen genutzt werden (orange und/ oder grün).
KLT Berlin gemeinnützige GmbH
Falkenhainer Weg 14, D-12489 Berlin
www.klt-bildung.example I Geschäftsführer: Jorinde Paskova, Lukas Drömberg I Amtsgericht Berlin-Charlottenburg, HRB 417592 B

```html
<!DOCTYPE html>
<html lang="de">
<head>
<meta charset="utf-8">
<title>KLT Berlin – Briefpapier</title>
<link rel="stylesheet" href="https://fonts.googleapis.com/css2?family=Lato:wght@400;700&family=Arimo:wght@400&display=swap">
<style>
  :root {
    --stage: #f1efec;
    --paper: #ffffff;
    --orange-light: #fbb877;
    --orange: #f7941e;
    --orange-text: #e5761f;
    --green: #acd03b;
    --ink: #1a1a1a;
    --grey: #555555;
    --footer-grey: #7a7a7a;
  }
  * { margin: 0; padding: 0; box-sizing: border-box; }
  html, body { width: 1200px; height: 2861px; overflow: hidden; }
  body { background: var(--stage); position: relative; }

  .letterhead {
    position: absolute;
    left: 60px; top: 665px;
    width: 1080px; height: 1530px;
    background: var(--paper);
    box-shadow: 0 6px 18px rgba(0,0,0,0.25);
    font-family: "Lato", sans-serif;
    color: var(--ink);
  }

  .side-band { position: absolute; left: 0; width: 72px; }
  .side-band--light { top: 0; height: 464px; background: var(--orange-light); }
  .side-band--orange { top: 464px; height: 232px; background: var(--orange); }
  .side-band--green { top: 696px; height: 228px; background: var(--green); }

  .brand {
    position: absolute; left: 124px; top: 130px;
    display: flex; align-items: center; gap: 14px;
  }
  .brand__mark { width: 30px; height: 30px; background: var(--orange-text); }
  .brand__name {
    font-family: "Lato", sans-serif; font-weight: 700;
    font-size: 44px; letter-spacing: 3px; color: var(--orange-text);
  }

  .sender {
    position: absolute; right: 104px; top: 126px;
    text-align: right; font-size: 19.5px; line-height: 24px; color: var(--grey);
  }
  .sender__org { color: var(--orange-text); }

  .memo-fields {
    position: absolute; left: 124px; top: 314px;
    font-size: 17px; line-height: 27px; border-collapse: collapse;
  }
  .memo-fields th { text-align: left; font-weight: 700; width: 65px; padding: 0; }
  .memo-fields td { padding: 0; color: var(--ink); }

  .body-copy {
    position: absolute; left: 124px; top: 512px; width: 852px;
    font-family: "Arimo", Arial, sans-serif; font-size: 18.6px; line-height: 24px;
    text-align: justify; color: var(--ink);
  }
  .body-copy p + p { margin-top: 24px; }

  .legal-footer {
    position: absolute; left: 0; right: 0; top: 1478px;
    text-align: center; font-size: 16.5px; color: var(--footer-grey);
  }
  .legal-footer .sep { color: var(--green); margin: 0 4px; }
</style>
</head>
<body>
  <article class="letterhead">
    <div class="side-band side-band--light"></div>
    <div class="side-band side-band--orange"></div>
    <div class="side-band side-band--green"></div>

    <div class="brand">
      <span class="brand__mark"></span>
      <span class="brand__name">KLT BERLIN</span>
    </div>

    <address class="sender" style="font-style:normal">
      <div class="sender__org">KLT Berlin gemeinnützige GmbH</div>
      <div>Falkenhainer Weg 14, D-12489 Berlin</div>
      <div>Tel.: +49 30 55 81 24 07</div>
      <div>E-Mail: mail@klt-bildung.example</div>
    </address>

    <table class="memo-fields">
      <tr><th>To:</th><td>[Recepient Name]</td></tr>
      <tr><th>From:</th><td>[Your Name]</td></tr>
      <tr><th>Cc:</th><td>[Name]</td></tr>
      <tr><th>Date:</th><td>[Date]</td></tr>
      <tr><th>Re:</th><td>[Subject]</td></tr>
    </table>

    <div class="body-copy">
      <p>Lorem ipsum dolor sit amet, consectetur adipiscing elit, sed do eiusmod tempor incididunt ut labore et dolore magna aliqua. Proin sagittis nisl rhoncus mattis rhoncus urna neque viverra. Sed vulputate odio ut enim blandit volutpat maecenas. Turpis in eu mi bibendum neque. Faucibus turpis in eu mi bibendum neque egestas. Massa vitae tortor condimentum lacinia quis vel eros donec. Erat pellentesque adipiscing commodo elit at imperdiet dui accumsan. Ullamcorper velit sed ullamcorper morbi. Vel facilisis volutpat est velit egestas dui. Sed lectus vestibulum mattis ullamcorper velit sed ullamcorper. Vestibulum morbi blandit cursus risus at ultrices mi tempus. Elit duis tristique sollicitudin nibh sit amet commodo nulla facilisi. Suspendisse interdum consectetur libero id. Sapien et ligula ullamcorper malesuada proin libero nunc consequat interdum. Sed vulputate odio ut enim blandit volutpat maecenas volutpat. Quis enim lobortis scelerisque fermentum dui.</p>
      <p>Praesent elementum facilisis leo vel. Enim facilisis gravida neque convallis a. Gravida arcu ac tortor dignissim convallis aenean et tortor at. Magna ac placerat vestibulum lectus mauris ultrices eros in. Bibendum est ultricies integer quis auctor elit. Odio morbi quis commodo odio aenean. Dolor sed viverra ipsum nunc aliquet bibendum enim facilisis. Iaculis urna id volutpat lacus laoreet. Posuere ac ut consequat semper viverra nam libero justo laoreet. Odio pellentesque diam volutpat commodo sed egestas egestas fringilla.</p>
      <p>Non arcu risus quis varius quam quisque id diam vel. Nunc scelerisque viverra mauris in aliquam sem fringilla. Vitae proin sagittis nisl rhoncus mattis. Pretium quam vulputate dignissim suspendisse in est ante. Sit amet est placerat in egestas erat imperdiet sed euismod. Dui ut ornare lectus sit amet est placerat in egestas. Diam phasellus vestibulum lorem sed risus ultricies tristique. In fermentum et sollicitudin ac. Blandit massa enim nec dui nunc mattis enim ut tellus. Egestas fringilla phasellus faucibus scelerisque eleifend donec pretium vulputate. Penatibus et magnis dis parturient montes.</p>
    </div>

    <footer class="legal-footer">
      www.klt-bildung.example<span class="sep">|</span>Geschäftsführer: Jorinde Paskova, Lukas Drömberg<span class="sep">|</span>Amtsgericht Berlin-Charlottenburg, HRB 417592 B
    </footer>
  </article>
</body>
</html>
```